Conference Header for use in marketing and on website

I need a header designed that promotes an event we will be holding to be used on marketing and website. I have attached a brief with the information that needs to be on it including the colours required. It will need to include an image of Melbourne at least and our logo. If you find a better Melbourne image you wish to use, I can purchase it off Corvel Imagery.

I want it to be eyecatching and exciting and vibrant while still providing the details clearly. I also want source files included.

```html
<!DOCTYPE html>
<html lang="en">
<head>
<meta charset="utf-8">
<title>ROTOFORM Conference &amp; Exhibition 2022 – Melbourne</title>
<link rel="stylesheet" href="https://fonts.googleapis.com/css2?family=Montserrat:ital,wght@0,300;0,600;0,700;0,800;1,300;1,600;1,700;1,800&display=swap">
<style>
  :root {
    --page-bg: #cfcfcf;
    --brand-purple: #6b2d91;
    --accent-blue: #3fbcef;
    --accent-blue-soft: rgba(47, 182, 240, 0.62);
    --white: #ffffff;
    --outline-grey: #d4d4d4;
    --sky-top: #8fc3ea;
    --sky-mid: #cfe2ef;
    --city-warm: #b98a5c;
    --foliage: #3f5a2e;
    --river: #1f3e66;
    --river-deep: #142c4c;
  }
  * { margin: 0; padding: 0; box-sizing: border-box; }
  html, body {
    width: 1200px; height: 666px; overflow: hidden;
    background: var(--page-bg);
    font-family: "Montserrat", Arial, sans-serif;
  }
  .banner {
    position: absolute; left: 69px; top: 68px;
    width: 1062px; height: 530px; overflow: hidden;
    color: var(--white);
  }
  .city-photo {
    position: absolute; inset: 0;
    background:
      linear-gradient(180deg,
        var(--sky-top) 0%, var(--sky-mid) 28%,
        var(--city-warm) 44%, #8a7a62 56%,
        var(--foliage) 66%, var(--river) 76%, var(--river-deep) 100%);
  }
  .blue-wash {
    position: absolute; left: 720px; top: 155px;
    width: 420px; height: 420px; border-radius: 50%;
    background: var(--accent-blue-soft);
  }
  .logo-tab {
    position: absolute; left: 0; top: 0;
    width: 236px; height: 101px;
    background: var(--white);
    border-bottom-right-radius: 48px;
    display: flex; align-items: center; gap: 12px;
    padding-left: 22px;
  }
  .logo-tab .logo-dot {
    width: 40px; height: 40px; border-radius: 50%;
    background: var(--brand-purple);
  }
  .logo-tab .logo-name {
    font-weight: 600; font-size: 40px; letter-spacing: 1px;
    color: var(--brand-purple);
  }
  .event-title {
    position: absolute; left: 262px; top: 18px; line-height: 1;
  }
  .event-title .name {
    font-weight: 300; font-size: 38px; letter-spacing: 1px;
  }
  .event-title .sub {
    font-weight: 700; font-style: italic; font-size: 21px; margin-top: 4px;
  }
  .location {
    position: absolute; right: 190px; top: 22px;
    text-align: right; line-height: 1.05;
  }
  .location .city {
    font-weight: 700; font-style: italic; font-size: 25px;
    display: flex; align-items: center; gap: 8px; justify-content: flex-end;
  }
  .location .country {
    font-weight: 300; font-style: italic; font-size: 25px;
  }
  .date-tab {
    position: absolute; right: 0; top: 0;
    width: 166px; height: 101px;
    background: var(--brand-purple);
    border-bottom-left-radius: 40px;
    text-align: center; padding-top: 20px; line-height: 1;
  }
  .date-tab .days { font-weight: 800; font-style: italic; font-size: 36px; }
  .date-tab .month { font-weight: 800; font-style: italic; font-size: 18px; margin-top: 2px; }
  .year-mark {
    position: absolute; left: 760px; top: 185px;
  }
  .tagline { position: absolute; left: 26px; top: 395px; }
  .tagline .quote { position: absolute; left: 0; top: 0; }
  .tagline .line-main {
    position: absolute; left: 72px; top: 14px;
    padding: 0 8px 0 4px;
    background: linear-gradient(90deg, transparent 0, var(--accent-blue) 30px);
    font-weight: 800; font-style: italic; font-size: 50px; line-height: 1; white-space: nowrap;
  }
  .tagline .line-sub {
    position: absolute; left: 98px; top: 72px; white-space: nowrap;
    font-weight: 800; font-style: italic; font-size: 44px; line-height: 1;
  }
  .tagline .line-sub small {
    font-size: 20px; font-weight: 700; margin-right: 10px; vertical-align: 6px;
  }
</style>
</head>
<body>
  <main class="banner">
    <div class="city-photo" role="img" aria-label="Photo of the Melbourne skyline at sunrise with a stone bridge across the river and hot air balloons in the sky"></div>
    <div class="blue-wash"></div>

    <div class="logo-tab">
      <span class="logo-dot"></span>
      <span class="logo-name">RFGO</span>
    </div>

    <header class="event-title">
      <div class="name">ROTOFORM</div>
      <div class="sub">Conference &amp; Exhibition</div>
    </header>

    <div class="location">
      <div class="city">
        <svg width="20" height="28" viewBox="0 0 20 28" aria-hidden="true">
          <path d="M10 0C4.5 0 0 4.4 0 9.8 0 17 10 28 10 28s10-11 10-18.2C20 4.4 15.5 0 10 0z" fill="var(--brand-purple)"/>
          <circle cx="10" cy="9.8" r="4" fill="var(--white)"/>
        </svg>
        Melbourne
      </div>
      <div class="country">Australia</div>
    </div>

    <div class="date-tab">
      <div class="days">18-20</div>
      <div class="month">September</div>
    </div>

    <svg class="year-mark" width="280" height="320" viewBox="0 0 280 320" role="img" aria-label="2022">
      <defs>
        <linearGradient id="yearFill" x1="0" y1="0" x2="1" y2="1">
          <stop offset="0" stop-color="#6b5a52"/>
          <stop offset="0.5" stop-color="#3a3f52"/>
          <stop offset="1" stop-color="#2a2a30"/>
        </linearGradient>
      </defs>
      <g font-family="Montserrat, Arial, sans-serif" font-weight="800" font-size="175"
         fill="url(#yearFill)" stroke="var(--outline-grey)" stroke-width="4" paint-order="stroke">
        <text x="0" y="148" letter-spacing="-6">20</text>
        <text x="0" y="305" letter-spacing="-6">22</text>
      </g>
    </svg>

    <div class="tagline">
      <svg class="quote" width="70" height="56" viewBox="0 0 70 56" aria-hidden="true">
        <g fill="none" stroke="var(--white)" stroke-width="3">
          <path d="M30 4C16 8 6 20 6 36c0 8 5 14 12 14s11-5 11-11-4-10-10-10c0-8 5-14 13-17z"/>
          <path d="M64 4C50 8 40 20 40 36c0 8 5 14 12 14s11-5 11-11-4-10-10-10c0-8 5-14 13-17z"/>
        </g>
      </svg>
      <div class="line-main">Reconnect</div>
      <div class="line-sub"><small>with</small>Relevance</div>
    </div>
  </main>
</body>
</html>
```